Small consulting business needs logo and business card design

I need a logo, business card and letterhead design for a small consulting firm called Kestrawell Consulting. My customers are generally small to medium sized businesses but I have done work for major corporates and government departments. The field of consulting is strategic/business planning and program management. I have blue as the predominate colour in my current business card but I am happy to change this for the right design
Industry/Entity Type
Business

```html
<!DOCTYPE html>
<html lang="en">
<head>
<meta charset="utf-8">
<title>Kestrawell Consulting – Letterhead</title>
<link rel="stylesheet" href="https://fonts.googleapis.com/css2?family=Cormorant+Garamond:wght@500&family=Tinos&display=swap">
<style>
  :root {
    --backdrop: #dcdcdc;
    --paper: #ffffff;
    --ink-black: #1f1d1e;
    --gold: #a98a3a;
    --gold-light: #d6b94f;
    --watermark: #f3efe4;
    --contact-ink: #2a2a2a;
  }
  * { margin: 0; padding: 0; box-sizing: border-box; }
  html, body {
    width: 1200px;
    height: 795px;
    overflow: hidden;
    background: var(--backdrop);
  }
  .letterhead {
    position: absolute;
    left: 345px;
    top: 40px;
    width: 510px;
    height: 715px;
    background: var(--paper);
    overflow: hidden;
  }
  .letterhead__company {
    position: absolute;
    top: 34px;
    right: 40px;
    font-family: "Cormorant Garamond", serif;
    font-weight: 500;
    font-size: 25px;
    color: var(--gold);
    letter-spacing: 0.3px;
  }
  .letterhead__watermark {
    position: absolute;
    top: 255px;
    left: 0;
    width: 100%;
    text-align: center;
    font-family: "Cormorant Garamond", serif;
    font-weight: 500;
    font-size: 64px;
    color: var(--watermark);
  }
  .letterhead__band {
    position: absolute;
    left: 0;
    top: 0;
    width: 510px;
    height: 715px;
  }
  .letterhead__band path { fill: var(--ink-black); }
  .letterhead__contact {
    position: absolute;
    top: 318px;
    right: 34px;
    text-align: right;
    font-family: "Tinos", serif;
    font-size: 11px;
    line-height: 13px;
    letter-spacing: 1px;
    color: var(--contact-ink);
  }
  .letterhead__brand {
    position: absolute;
    left: 34px;
    bottom: 34px;
    display: flex;
    align-items: center;
    gap: 10px;
  }
  .letterhead__brand-square {
    width: 18px;
    height: 18px;
    background: var(--gold-light);
  }
  .letterhead__brand-name {
    font-family: "Cormorant Garamond", serif;
    font-weight: 500;
    font-size: 22px;
    color: var(--gold-light);
  }
</style>
</head>
<body>
  <main class="letterhead">
    <h1 class="letterhead__company">Kestrawell Consulting</h1>
    <div class="letterhead__watermark" aria-hidden="true">Kestrawell</div>
    <svg class="letterhead__band" viewBox="0 0 510 715" aria-hidden="true">
      <path d="M510,360 C470,520 260,615 0,640 L0,715 L510,715 Z"/>
    </svg>
    <address class="letterhead__contact">
      Street Address<br>
      M:1234 567 890<br>
      E:abc@kestrawell.com
    </address>
    <div class="letterhead__brand">
      <span class="letterhead__brand-square"></span>
      <span class="letterhead__brand-name">Kestrawell</span>
    </div>
  </main>
</body>
</html>
```